business card design for luxurious real estate brand

using the attached logo, i am looking for a 2-sided business card design. the back should be the gold logo on black background. the front needs to include: gold logo, name, phone, email, and website

Industry/Entity Type

real estate

Contact Information for Business Card

logo, name, email, phone, website

Font styles to use
Sans Serif

```html
<!DOCTYPE html>
<html lang="en">
<head>
<meta charset="utf-8">
<title>Casa Verano – Business Card</title>
<link rel="stylesheet" href="https://fonts.googleapis.com/css2?family=Open+Sans:wght@400;600;700&display=swap">
<style>
  :root {
    --stage: #161616;
    --card: #231f20;
    --gold: #ffca05;
    --grey: #545454;
    --white: #ffffff;
    --pattern-a: #2a2627;
    --pattern-b: #1b1819;
  }
  * { margin: 0; padding: 0; box-sizing: border-box; }
  html, body { width: 1200px; height: 1000px; overflow: hidden; }
  body {
    background: var(--stage);
    font-family: "Open Sans", Arial, sans-serif;
    position: relative;
  }
  .card {
    position: absolute;
    left: 220px;
    width: 760px;
    height: 434px;
    background: var(--card);
    overflow: hidden;
    box-shadow: 0 10px 30px rgba(0,0,0,.5);
  }
  .card--front { top: 46px; }
  .card--back { top: 520px; }
  .card__art { position: absolute; inset: 0; }

  .brand {
    position: absolute;
    display: flex;
    align-items: center;
    gap: 12px;
    color: var(--gold);
    font-weight: 600;
    letter-spacing: 4px;
    text-transform: uppercase;
    white-space: nowrap;
  }
  .brand__mark { width: 22px; height: 22px; background: var(--gold); flex: none; }
  .card--front .brand { top: 120px; right: 70px; font-size: 22px; }
  .card--back .brand { top: 190px; right: 56px; font-size: 20px; }

  .contact { position: absolute; left: 48px; top: 232px; color: var(--white); }
  .contact__name {
    color: var(--gold);
    font-weight: 700;
    font-size: 23px;
    line-height: 1.1;
    text-transform: uppercase;
  }
  .contact__role { font-size: 16px; margin: 2px 0 12px 8px; }
  .contact__list { list-style: none; margin-left: 14px; }
  .contact__item {
    display: flex; align-items: center; gap: 8px;
    font-size: 15px; line-height: 22px;
  }
  .contact__icon { width: 14px; height: 14px; flex: none; }

  .pattern { position: absolute; inset: 0; background: linear-gradient(135deg, var(--pattern-a), var(--pattern-b)); }
</style>
</head>
<body>

<section class="card card--front" aria-label="Business card front">
  <svg class="card__art" viewBox="0 0 760 434" aria-hidden="true">
    <line x1="232" y1="250" x2="716" y2="250" stroke="var(--gold)" stroke-width="2"/>
    <rect x="0" y="250" width="12" height="46" fill="var(--gold)"/>
    <polygon points="392,316 760,316 760,325 401,325" fill="var(--gold)"/>
    <polygon points="413,334 760,334 760,434 513,434" fill="var(--grey)"/>
    <polygon points="0,372 385,372 447,434 0,434" fill="var(--gold)"/>
  </svg>

  <div class="brand"><span class="brand__mark"></span>Casa Verano</div>

  <div class="contact">
    <p class="contact__name">Marcus Hale</p>
    <p class="contact__role">Founder</p>
    <ul class="contact__list">
      <li class="contact__item">
        <svg class="contact__icon" viewBox="0 0 16 16"><path fill="var(--gold)" d="M3 1h3l1 4-2 1.5a9 9 0 0 0 4.5 4.5L11 9l4 1v3a2 2 0 0 1-2 2C7 15 1 9 1 3a2 2 0 0 1 2-2z"/></svg>
        (555) 204-3180
      </li>
      <li class="contact__item">
        <svg class="contact__icon" viewBox="0 0 16 16"><rect x="1" y="3" width="14" height="10" rx="1" fill="var(--gold)"/><path d="M1.5 3.5 8 9l6.5-5.5" fill="none" stroke="var(--card)" stroke-width="1.4"/></svg>
        hello@casaverano.com
      </li>
      <li class="contact__item">
        <svg class="contact__icon" viewBox="0 0 16 16"><circle cx="8" cy="8" r="7" fill="var(--gold)"/><path d="M1 8h14M8 1c-3 3.5-3 10.5 0 14M8 1c3 3.5 3 10.5 0 14" fill="none" stroke="var(--card)" stroke-width="1.1"/></svg>
        www.casaverano.com
      </li>
    </ul>
  </div>
</section>

<section class="card card--back" aria-label="Business card back">
  <div class="pattern" role="img" aria-label="Faint tone-on-tone repeating brand pattern across the card"></div>
  <div class="brand"><span class="brand__mark"></span>Casa Verano</div>
</section>

</body>
</html>
```